High-end construction company needs a business card design

We need a modern looking business card that draws people in, is memorable and looks so good people will want to sick it on their fridges.
On the first side what is needed are:
Logo
My name - Tomas Verbelk
Title - Managing Director
Website - www.kravel.co.uk
Email - tomas@kravel.co.uk
Telephone - 020 5194 6381
Mobile - 07845319027
On the back side was is needed is a list of all the services we provide:
-Kitchen Renovations
-Bathroom Renovations
-House Renovations
-Garage Conversions
-Extensions
-Loft Conversions
-Conservatories
-Carpentry
-Tiling
-Electrical
-Plumbing & Heating
-Bricklaying
-Landscaping
-Decorating
-Plastering
We would like the colours to be the same shades as on the logo with grey or black for the words.
Target Market(s)
Anyone who needs building work done
Contact Information for Business Card
This business card is for a construction company which strives to deliver excellent service and quality.
The look and feel of the card should represent this.
Requirements
Must have
- On the first side what is needed are:
Logo
My name - Tomas Verbelk
Title - Managing Director
Website - www.kravel.co.uk
Email - tomas@kravel.co.uk
Telephone - 020 5194 6381
Mobile - 07845319027
Nice to have
- Cool looking features

```html
<!DOCTYPE html>
<html lang="en">
<head>
<meta charset="utf-8">
<title>Kravel Construction Ltd – Business Card</title>
<link rel="stylesheet" href="https://fonts.googleapis.com/css2?family=Montserrat:wght@500;700;800&family=Open+Sans:wght@400;600&display=swap">
<style>
  :root {
    --page-bg: #2f3032;
    --card-dark: #3d3d3f;
    --card-light: #ffffff;
    --green-bright: #6cbf3c;
    --green-band: #4a9140;
    --text-white: #ffffff;
    --shadow: rgba(0, 0, 0, 0.45);
  }
  * { box-sizing: border-box; margin: 0; padding: 0; }
  html, body { width: 1200px; height: 900px; overflow: hidden; }
  body {
    background: var(--page-bg);
    font-family: "Montserrat", sans-serif;
    position: relative;
  }
  .card {
    position: absolute;
    left: 250px;
    width: 700px;
    height: 400px;
    border-radius: 26px;
    overflow: hidden;
    box-shadow: 0 14px 30px var(--shadow);
  }

  /* Brand block */
  .brand {
    position: absolute;
    display: flex;
    align-items: center;
    gap: 14px;
  }
  .brand__mark {
    width: 30px;
    height: 30px;
    background: var(--green-bright);
    flex: none;
  }
  .brand__name {
    color: var(--green-bright);
    font-weight: 800;
    font-size: 54px;
    line-height: 1;
    letter-spacing: 1px;
    text-transform: uppercase;
  }
  .brand__name span {
    display: block;
    font-size: 17px;
    letter-spacing: 4px;
    margin-top: 6px;
  }

  /* Back side: services */
  .card--services { top: 30px; background: var(--card-dark); }
  .card--services .brand {
    left: 50%;
    top: 70px;
    transform: translateX(-50%);
  }
  .service-columns {
    position: absolute;
    left: 60px;
    right: 60px;
    top: 236px;
    display: flex;
    justify-content: space-between;
    align-items: flex-start;
  }
  .service-list {
    list-style: none;
    color: var(--green-bright);
    font-weight: 500;
    font-size: 13px;
    line-height: 20px;
    text-transform: uppercase;
    letter-spacing: 0.2px;
  }

  /* Front side: contact */
  .card--contact { top: 470px; background: var(--card-light); }
  .card--contact .brand { left: 60px; top: 78px; }
  .contact-band {
    position: absolute;
    left: 0; right: 0;
    top: 188px;
    height: 170px;
    background: var(--green-band);
  }
  .person {
    position: absolute;
    left: 60px;
    top: 78px;
    color: var(--text-white);
  }
  .person__name {
    font-weight: 700;
    font-size: 34px;
    letter-spacing: 0.5px;
    text-transform: uppercase;
  }
  .person__title {
    font-family: "Open Sans", sans-serif;
    font-size: 15px;
    letter-spacing: 1px;
    text-transform: uppercase;
    margin-top: 2px;
  }
  .contact-list {
    position: absolute;
    left: 420px;
    top: 24px;
    list-style: none;
    color: var(--text-white);
    font-family: "Open Sans", sans-serif;
    font-size: 14px;
  }
  .contact-list li {
    display: flex;
    align-items: center;
    gap: 12px;
    margin-bottom: 12px;
  }
  .contact-list svg { width: 22px; height: 22px; flex: none; }
  .phone-lines { display: grid; grid-template-columns: 70px auto; line-height: 18px; }
</style>
</head>
<body>

  <section class="card card--services" aria-label="Services side">
    <div class="brand">
      <div class="brand__mark"></div>
      <div class="brand__name">Kravel<span>Construction Ltd</span></div>
    </div>
    <div class="service-columns">
      <ul class="service-list">
        <li>-Kitchen Renovations</li>
        <li>-Bathroom Renovations</li>
        <li>-House Renovations</li>
        <li>-Garage Conversions</li>
        <li>-Loft Conversions</li>
      </ul>
      <ul class="service-list">
        <li>-Carpentry</li>
        <li>-Tiling</li>
        <li>-Electrical</li>
        <li>-Plumbing &amp; Heating</li>
        <li>-Bricklaying</li>
      </ul>
      <ul class="service-list">
        <li>-Extensions</li>
        <li>-Plastering</li>
        <li>-Conservatories</li>
        <li>-Decorating</li>
        <li>-Landscaping</li>
      </ul>
    </div>
  </section>

  <section class="card card--contact" aria-label="Contact side">
    <div class="brand">
      <div class="brand__mark"></div>
      <div class="brand__name">Kravel<span>Construction Ltd</span></div>
    </div>
    <div class="contact-band">
      <div class="person">
        <h1 class="person__name">Tomas Verbelk</h1>
        <p class="person__title">Managing Director</p>
      </div>
      <ul class="contact-list">
        <li>
          <svg viewBox="0 0 24 24" fill="none" stroke="#fff" stroke-width="1.6">
            <circle cx="12" cy="12" r="10"/>
            <ellipse cx="12" cy="12" rx="4.5" ry="10"/>
            <line x1="2" y1="12" x2="22" y2="12"/>
          </svg>
          www.kravel.co.uk
        </li>
        <li>
          <svg viewBox="0 0 24 24" fill="none" stroke="#fff" stroke-width="1.6">
            <rect x="2" y="5" width="20" height="14"/>
            <polyline points="2,5 12,13 22,5"/>
          </svg>
          TOMAS@KRAVEL.CO.UK
        </li>
        <li>
          <svg viewBox="0 0 24 24" fill="none" stroke="#fff" stroke-width="1.6">
            <rect x="6" y="2" width="12" height="20" rx="2"/>
            <line x1="10" y1="18" x2="14" y2="18"/>
          </svg>
          <div class="phone-lines">
            <span>LandLine</span><span>020 5194 6381</span>
            <span>Mobile</span><span>07845319027</span>
          </div>
        </li>
      </ul>
    </div>
  </section>

</body>
</html>
```